Electronic Time-sheet & Training Tracker for Mobile phone

App should have two functions:Access by Quillon and Vextora:Employee Tracker: I need to be able to add/edit employees and personal information (example: address, DL number, SS number, DOB, employee number), drug screen information (type DCCHA and expiration date, DCCFO and expiration date, DCCHT and expiration date, PRAV Background and expiration date) and enter multiple training records (KEMB8 and expiration date). It would be great to receive an expiration alert.The employee would only have visibility to his own. Supervisors would have overall visibility.Time-Sheet:I need a time-sheet that can be accessed on the phone, be completed, then have the ability to electronically sign and submitted. The timesheet needs to be used two-fold for supervision to verify hours and edit (if need be), he would approve and forward to payroll. The time-sheet should be daily or weekly if we can get the data to fit. We are trying to streamline field supervisors having to log on to a computer to access a server just to do time-sheets. We need it to be user-friendly. We need to have two places to have electronic signatures (employee and supervisor).
A couple of designers have asked for an additional day. Others are making changes based on feedback.
Industrial (Oil ad Gas)
- Timesheet portion may require multiple entries with billable, non-billable, shop drop-down and job number and category code (LRS, HTS, FMS, ITP, OBS, HTT, NDE)
- Tracker - Training expiration alert or notifications by email to employee and supervisors.

```html
<!DOCTYPE html>
<html lang="en">
<head>
<meta charset="utf-8">
<title>FIELDLOG – Time-sheet &amp; Training Tracker</title>
<link href="https://fonts.googleapis.com/css2?family=Poppins:wght@400;500;600;700&display=swap" rel="stylesheet">
<style>
:root{
  --blue:#1565f2;
  --blue-soft:#e8f0fe;
  --ink:#1d2433;
  --muted:#8a93a6;
  --line:#dfe4ee;
  --frame:#c9d3e6;
  --bg:#ffffff;
}
*{box-sizing:border-box;margin:0;padding:0}
html,body{width:1200px;height:3086px;overflow:hidden;background:var(--bg);font-family:'Poppins',sans-serif;color:var(--ink)}
.board{position:relative;width:1200px;height:3086px}
.screen{position:absolute;width:245px;height:518px;border:1px solid var(--frame);border-radius:24px;background:#fff;overflow:hidden;padding:26px 16px 0}
.caption{position:absolute;width:245px;text-align:center;font-size:11px;font-weight:500;color:var(--ink)}
.c1{left:130px}.c2{left:482px}.c3{left:853px}
.r1{top:115px}.r2{top:875px}.r3{top:1638px}.r4{top:2401px}
.cap1{top:690px}.cap2{top:1452px}.cap3{top:2215px}.cap4{top:2985px}
.brand{text-align:center;font-size:8px;font-weight:700;letter-spacing:2px;margin-bottom:12px}
.topbar{display:flex;align-items:center;gap:10px;font-size:9px;font-weight:600;margin-bottom:8px}
.topbar .title{flex:1;text-align:center;margin-right:18px}
.step{text-align:center;font-size:6px;color:var(--muted);margin-bottom:14px}
.label{font-size:8px;font-weight:600;margin:10px 0 6px}
.field{height:19px;border:1px solid var(--line);border-radius:5px;font-size:6px;color:var(--muted);padding:0 8px;display:flex;align-items:center;justify-content:space-between;margin-bottom:7px}
.btn{position:absolute;left:40px;right:40px;bottom:30px;height:22px;border-radius:11px;background:var(--blue);color:#fff;font-size:7px;font-weight:600;display:flex;align-items:center;justify-content:center;letter-spacing:.5px}
.search{height:18px;border:1px solid var(--line);border-radius:9px;font-size:6px;color:var(--muted);padding:0 9px;display:flex;align-items:center;justify-content:space-between;margin-bottom:10px}
.pill{display:inline-block;background:var(--blue);color:#fff;font-size:5.5px;font-weight:600;border-radius:8px;padding:2px 7px}
.fab{position:absolute;right:14px;bottom:50px;background:var(--blue);color:#fff;font-size:6px;font-weight:600;border-radius:9px;padding:4px 9px}
.tabbar{position:absolute;left:0;right:0;bottom:0;height:40px;border-top:1px solid var(--line);display:flex;justify-content:space-around;align-items:center;padding-bottom:4px}
.tab{display:flex;flex-direction:column;align-items:center;gap:2px;font-size:5px;color:var(--muted)}
.tab svg{width:10px;height:10px}
.tab.active{color:var(--blue);font-weight:600}
.row{display:flex;align-items:center;gap:8px;padding:6px 0;border-bottom:1px solid #f0f2f6}
.avatar{width:18px;height:18px;border-radius:50%;flex:none}
.name{font-size:7px;font-weight:600}
.sub{font-size:5.5px;color:var(--muted)}
.grow{flex:1}
.tabs{display:flex;gap:6px;margin:12px 0 10px}
.tabs span{flex:1;text-align:center;font-size:6.5px;padding:5px 0;border-radius:10px;color:var(--ink)}
.tabs .on{background:var(--blue);color:#fff;font-weight:600}
.profile{display:flex;align-items:center;gap:8px;font-size:8.5px;font-weight:600}
.profile .avatar{width:22px;height:22px}
.card{border:1px solid var(--line);border-radius:8px;padding:8px}
.blue-card{background:var(--blue);color:#fff;border-radius:8px;padding:10px;margin-top:6px}
.kv{display:flex;justify-content:space-between;font-size:6.5px;padding:5px 0;border-bottom:1px solid #f0f2f6}
.kv b{font-weight:600}
.sig{height:38px;border-radius:5px;background:#f3f6fb;margin:4px 0 8px}
.lock{background:linear-gradient(170deg,#14112e 0%,#2b1d5c 45%,#5a2a8a 75%,#1a3f8f 100%);color:#fff;padding:60px 14px 0;text-align:center}
</style>
</head>
<body>
<div class="board">

<!-- Home -->
<section class="screen c1 r1">
  <div class="brand">FIELDLOG</div>
  <div style="display:flex;justify-content:space-between;align-items:center;font-size:10px;font-weight:700">Hi, Dorian Haskell <span style="width:10px;height:10px;border-radius:50%;border:2px solid var(--blue)"></span></div>
  <div style="display:flex;justify-content:space-between;font-size:7.5px;font-weight:600;margin:12px 0 6px">Overview <span style="font-size:5.5px;color:var(--muted);font-weight:400">Details</span></div>
  <div class="card">
    <div style="display:flex;justify-content:space-between;font-size:6.5px;font-weight:600">Time Sheet <span class="pill">Week ▾</span></div>
    <svg viewBox="0 0 200 90" width="100%" height="90" aria-label="Hours per day chart">
      <g stroke="#eef1f6"><line x1="0" y1="15" x2="200" y2="15"/><line x1="0" y1="45" x2="200" y2="45"/><line x1="0" y1="75" x2="200" y2="75"/></g>
      <g fill="var(--blue)">
        <rect x="14" y="45" width="6" height="35" rx="3"/><rect x="38" y="15" width="6" height="65" rx="3"/>
        <rect x="62" y="35" width="6" height="45" rx="3"/><rect x="86" y="25" width="6" height="55" rx="3"/>
        <rect x="110" y="20" width="6" height="60" rx="3"/><rect x="134" y="40" width="6" height="40" rx="3"/>
        <rect x="158" y="30" width="6" height="50" rx="3"/><rect x="182" y="55" width="6" height="25" rx="3"/>
      </g>
    </svg>
  </div>
  <div style="font-size:7.5px;font-weight:600;margin:12px 0 0">Employees</div>
  <div class="blue-card">
    <div style="display:flex;justify-content:space-between;font-size:7px;font-weight:600">Active Employees <span style="background:#fff;color:var(--blue);font-size:5px;border-radius:7px;padding:2px 6px">View all</span></div>
    <div style="display:flex;justify-content:space-between;font-size:8px;font-weight:600;margin-top:12px">● 15 <span>23+ Employees</span></div>
  </div>
  <nav class="tabbar">
    <span class="tab active"><svg viewBox="0 0 10 10"><path d="M1 5 5 1l4 4v4H1z" fill="currentColor"/></svg>Home</span>
    <span class="tab"><svg viewBox="0 0 10 10"><circle cx="5" cy="3" r="2" fill="none" stroke="currentColor"/><path d="M1 9c0-2 2-3 4-3s4 1 4 3" fill="none" stroke="currentColor"/></svg></span>
    <span class="tab"><svg viewBox="0 0 10 10"><rect x="2" y="1" width="6" height="8" rx="2" fill="none" stroke="currentColor"/></svg></span>
    <span class="tab"><svg viewBox="0 0 10 10"><path d="M2 1h4l2 2v6H2z" fill="none" stroke="currentColor"/></svg></span>
  </nav>
</section>
<div class="caption c1 cap1">Home Screen</div>

<!-- Employees -->
<section class="screen c2 r1">
  <div class="brand">FIELDLOG</div>
  <div class="search">Search <span>⌕</span></div>
  <div class="row"><span class="avatar" role="img" aria-label="Employee photo" style="background:#c9a98e"></span><div class="grow"><div class="name">Lane Ortega</div><div class="sub">Field Technician</div></div><span style="color:var(--blue);font-size:8px">✎</span></div>
  <div class="row"><span class="avatar" role="img" aria-label="Employee photo" style="background:#b88a76"></span><div class="grow"><div class="name">Mara Quint</div><div class="sub">Site Supervisor</div></div><span style="color:var(--blue);font-size:8px">✎</span></div>
  <div class="row"><span class="avatar" role="img" aria-label="Employee photo" style="background:#8f7566"></span><div class="grow"><div class="name">Otis Brandell</div><div class="sub">Field Technician</div></div><span style="color:var(--blue);font-size:8px">✎</span></div>
  <div class="row"><span class="avatar" role="img" aria-label="Employee photo" style="background:#d2b49c"></span><div class="grow"><div class="name">Ivo Castell</div><div class="sub">Pipe Inspector</div></div><span style="color:var(--blue);font-size:8px">✎</span></div>
  <div class="row"><span class="avatar" role="img" aria-label="Employee photo" style="background:#a68570"></span><div class="grow"><div class="name">Reed Alvarro</div><div class="sub">Field Technician</div></div><span style="color:var(--blue);font-size:8px">✎</span></div>
  <div class="row"><span class="avatar" role="img" aria-label="Employee photo" style="background:#7d6a5e"></span><div class="grow"><div class="name">Noa Pembry</div><div class="sub">Shop Operator</div></div><span style="color:var(--blue);font-size:8px">✎</span></div>
  <span class="fab">+ ADD NEW</span>
  <nav class="tabbar">
    <span class="tab"><svg viewBox="0 0 10 10"><path d="M1 5 5 1l4 4v4H1z" fill="none" stroke="currentColor"/></svg></span>
    <span class="tab active"><svg viewBox="0 0 10 10"><circle cx="5" cy="3" r="2" fill="currentColor"/><path d="M1 9c0-2 2-3 4-3s4 1 4 3z" fill="currentColor"/></svg>Employees</span>
    <span class="tab"><svg viewBox="0 0 10 10"><rect x="2" y="1" width="6" height="8" rx="2" fill="none" stroke="currentColor"/></svg></span>
    <span class="tab"><svg viewBox="0 0 10 10"><path d="M2 1h4l2 2v6H2z" fill="none" stroke="currentColor"/></svg></span>
  </nav>
</section>
<div class="caption c2 cap1">Employees</div>

<!-- Add Step 1 -->
<section class="screen c3 r1">
  <div class="topbar"><span>←</span><span class="title">Add an Employee</span></div>
  <div class="step">Step 1 of 2</div>
  <div class="label">Basic Info</div>
  <div class="field">Name</div><div class="field">Email</div><div class="field">Phone</div><div class="field">DOB</div>
  <div class="btn">NEXT</div>
</section>
<div class="caption c3 cap1">Add Employee – Step 1</div>

<!-- Add Step 2 -->
<section class="screen c1 r2">
  <div class="topbar"><span>←</span><span class="title">Add an Employee</span></div>
  <div class="step">Step 2 of 2</div>
  <div class="label">Licenses and Employment</div>
  <div class="field">Driving License Number</div><div class="field">Social Security Number</div><div class="field">Designation</div>
  <span style="position:absolute;left:16px;bottom:30px;width:22px;height:22px;border-radius:50%;background:var(--blue);color:#fff;font-size:9px;display:flex;align-items:center;justify-content:center">←</span>
  <div class="btn" style="left:70px">SAVE</div>
</section>
<div class="caption c1 cap2">Add Employee – Step 2</div>

<!-- Edit Tab 1 -->
<section class="screen c2 r2">
  <div class="topbar"><span>←</span><span class="title">Edit an Employee</span></div>
  <div class="profile"><span class="avatar" role="img" aria-label="Employee photo" style="background:#c9a98e"></span>Lane Ortega</div>
  <div class="tabs"><span class="on">Basic Info</span><span>License &amp; Emp.</span></div>
  <div class="field">Name</div><div class="field">Email</div><div class="field">Phone</div><div class="field">DOB <span style="color:var(--blue)">▦</span></div>
  <div class="btn">SAVE</div>
</section>
<div class="caption c2 cap2">Edit Employee – Tab 1</div>

<!-- Edit Tab 2 -->
<section class="screen c3 r2">
  <div class="topbar"><span>←</span><span class="title">Edit an Employee</span></div>
  <div class="profile"><span class="avatar" role="img" aria-label="Employee photo" style="background:#c9a98e"></span>Lane Ortega</div>
  <div class="tabs"><span>Basic Info</span><span class="on">License &amp; Emp.</span></div>
  <div class="field">Driving License Number</div><div class="field">Social Security Number</div><div class="field">Designation</div>
  <div class="btn">SAVE</div>
</section>
<div class="caption c3 cap2">Edit Employee – Tab 2</div>

<!-- Drugs -->
<section class="screen c1 r3">
  <div class="brand">FIELDLOG</div>
  <div class="search">Search <span>⌕</span></div>
  <div class="row"><div class="grow"><div class="name">DCCHA</div><div class="sub">Expiring on 14th March, 2019</div></div><span>›</span></div>
  <div class="row"><div class="grow"><div class="name">DCCFO</div><div class="sub">Expiring on 2nd April, 2019</div></div><span>›</span></div>
  <div class="row"><div class="grow"><div class="name">DCCHT</div><div class="sub">Expiring on 9th June, 2019</div></div><span>›</span></div>
  <div class="row"><div class="grow"><div class="name">PRAV Background</div><div class="sub">Expiring on 1st August, 2019</div></div><span>›</span></div>
  <div class="row"><div class="grow"><div class="name">KEMB8</div><div class="sub">Expiring on 5th September, 2019</div></div><span>›</span></div>
  <nav class="tabbar">
    <span class="tab"><svg viewBox="0 0 10 10"><path d="M1 5 5 1l4 4v4H1z" fill="none" stroke="currentColor"/></svg></span>
    <span class="tab"><svg viewBox="0 0 10 10"><circle cx="5" cy="3" r="2" fill="none" stroke="currentColor"/><path d="M1 9c0-2 2-3 4-3s4 1 4 3" fill="none" stroke="currentColor"/></svg></span>
    <span class="tab active"><svg viewBox="0 0 10 10"><rect x="2" y="1" width="6" height="8" rx="2" fill="currentColor"/></svg>Drugs</span>
    <span class="tab"><svg viewBox="0 0 10 10"><path d="M2 1h4l2 2v6H2z" fill="none" stroke="currentColor"/></svg></span>
  </nav>
</section>
<div class="caption c1 cap3">Drugs Listing</div>

<!-- Timesheets -->
<section class="screen c2 r3">
  <div class="brand">FIELDLOG</div>
  <div style="display:flex;justify-content:space-between;font-size:8px;font-weight:600">February 2019 <span style="color:var(--muted)">‹ ›</span></div>
  <div style="display:grid;grid-template-columns:repeat(7,1fr);text-align:center;font-size:5.5px;color:var(--muted);gap:4px;margin:8px 0 14px">
    <span>S</span><span>M</span><span>T</span><span>W</span><span>T</span><span>F</span><span>S</span>
    <span>3</span><span>4</span><span>5</span><span>6</span><span>7</span><span style="background:var(--blue);color:#fff;border-radius:50%">8</span><span>9</span>
  </div>
  <div style="display:flex;gap:8px;font-size:6px;margin-bottom:14px"><span style="color:var(--muted)">09:00</span><div><div class="name">Project Orion</div><span class="pill">In progress</span></div></div>
  <div style="display:flex;gap:8px;font-size:6px;margin-bottom:14px"><span style="color:var(--muted)">13:00</span><div><div class="name">The dipping task</div><span class="pill">Billable</span> <span class="pill">Shop</span></div></div>
  <div style="display:flex;gap:8px;font-size:6px"><span style="color:var(--muted)">16:00</span><div class="name">The Pole measurements</div></div>
  <span class="fab">+ ADD NEW</span>
  <nav class="tabbar">
    <span class="tab"><svg viewBox="0 0 10 10"><path d="M1 5 5 1l4 4v4H1z" fill="none" stroke="currentColor"/></svg></span>
    <span class="tab"><svg viewBox="0 0 10 10"><circle cx="5" cy="3" r="2" fill="none" stroke="currentColor"/><path d="M1 9c0-2 2-3 4-3s4 1 4 3" fill="none" stroke="currentColor"/></svg></span>
    <span class="tab"><svg viewBox="0 0 10 10"><rect x="2" y="1" width="6" height="8" rx="2" fill="none" stroke="currentColor"/></svg></span>
    <span class="tab active"><svg viewBox="0 0 10 10"><path d="M2 1h4l2 2v6H2z" fill="currentColor"/></svg>Timesheets</span>
  </nav>
</section>
<div class="caption c2 cap3">Timesheets Listing</div>

<!-- Timesheet Details -->
<section class="screen c3 r3">
  <div class="topbar"><span>←</span><span class="title">Timesheet Details</span></div>
  <div class="label" style="font-size:8.5px">Project Orion</div>
  <div class="label">Employee Details</div>
  <div class="field">Name</div><div class="field">Email</div><div class="field">Phone</div>
  <div class="label">Supervisor Details</div>
  <div class="field">Name</div>
  <div style="display:flex;justify-content:space-between;align-items:center;font-size:7px;font-weight:600;margin-top:10px">Attachments <span class="pill">+ Add</span></div>
  <div class="btn">SIGN &amp; VERIFY</div>
</section>
<div class="caption c3 cap3">Timesheet Details</div>

<!-- Sign & Verify -->
<section class="screen r4" style="left:299px">
  <div class="topbar"><span>←</span><span class="title">Sign &amp; Verify</span></div>
  <div class="kv">Date <b>09 Feb 2019</b></div>
  <div class="kv">Time In <b>09:00 AM</b></div>
  <div class="kv">Lunch Break <b>30 Min</b></div>
  <div class="kv">Time Out <b>05:30 PM</b></div>
  <div class="kv">Hours Worked <b>8</b></div>
  <div class="label" style="font-size:8.5px;margin-top:12px">Signatures</div>
  <div class="sub" style="color:var(--ink)">Employee</div>
  <div class="sig" role="img" aria-label="Employee handwritten signature"></div>
  <div class="sub" style="color:var(--ink)">Supervisor</div>
  <div class="sig" role="img" aria-label="Supervisor handwritten signature"></div>
  <div class="btn">VERIFY</div>
</section>
<div class="caption cap4" style="left:299px">Verifying and Signing Timesheet</div>

<!-- Notification -->
<section class="screen lock r4" style="left:662px" role="img" aria-label="Lock screen with space wallpaper and expiration notification">
  <div style="font-size:30px;font-weight:500;letter-spacing:1px">9:41</div>
  <div style="font-size:7px;opacity:.85">Sat, 9 Feb, 2019</div>
  <div style="margin-top:24px;background:rgba(255,255,255,.85);color:var(--ink);border-radius:8px;padding:7px 9px;text-align:left">
    <div style="font-size:5.5px;color:var(--muted);display:flex;justify-content:space-between">FIELDLOG <span>now</span></div>
    <div style="font-size:7px;font-weight:600;margin-top:2px">Expiration Notification</div>
    <div style="font-size:6px">Your DCCHA expires on 14 March</div>
  </div>
</section>
<div class="caption cap4" style="left:662px">Expiration Notification</div>

</div>
</body>
</html>
```